Birchford Realty Business Card

Business Card:

Somewhere on front of card, please include Broker License Number: 5839162

Website is BirchfordRealty.example

Address is:
7218 Crestover Ave E
Saginaw, MI 48271

I'll let you use creative freedom on the rest; we obviously need Name, Title, Email (@BirchfordRealty.example), Office Phone, Cell Phone.

Don't want any special die-cutting, just a standard size business card.

On the back, include a place for the date and time of an appointment to be written in pen.

Requirements
Must have
• Our logo, attached to email.

```html
<!DOCTYPE html>
<html lang="en">
<head>
<meta charset="utf-8">
<title>Birchford Realty Business Card</title>
<link rel="stylesheet" href="https://fonts.googleapis.com/css2?family=Crimson+Text:wght@400;600&display=swap">
<style>
  :root {
    --navy: #1d1f55;
    --white: #ffffff;
    --paper: #f4f4f6;
    --stage: #e9e7e3;
    --rule-grey: #9a9bb0;
  }
  * { margin: 0; padding: 0; box-sizing: border-box; }
  html, body {
    width: 1200px; height: 1000px; overflow: hidden;
    background: var(--stage);
    font-family: "Crimson Text", Georgia, serif;
  }
  .card {
    position: absolute; left: 250px;
    width: 700px; height: 400px;
    overflow: hidden;
    box-shadow: 0 8px 24px rgba(0,0,0,0.16);
  }

  /* Front */
  .card--front { top: 60px; background: var(--navy); color: var(--white); }
  .front__band {
    position: absolute; left: 0; bottom: 0;
    width: 100%; height: 50px; background: var(--paper);
  }
  .front__tab { position: absolute; bottom: 0; background: var(--paper); }
  .front__tab--left { left: 0; width: 100px; height: 125px; border-top-right-radius: 50px; }
  .front__tab--right { right: 0; width: 80px; height: 116px; border-top-left-radius: 40px; }
  .front__dot {
    position: absolute; right: 25px; bottom: 72px;
    width: 30px; height: 30px; border-radius: 50%; background: var(--navy);
  }
  .brand-name {
    position: absolute; left: 115px; top: 150px;
    font-weight: 600; font-size: 42px; line-height: 1;
  }
  .brand-rule {
    position: absolute; left: 115px; top: 205px;
    width: 270px; height: 2px; background: var(--white);
  }
  .company { position: absolute; left: 430px; top: 62px; }
  .company__name { font-size: 28px; line-height: 1.1; }
  .company__license { font-size: 13px; margin-top: 4px; opacity: 0.9; }
  .agent { margin-top: 14px; }
  .agent__name { font-size: 18px; font-weight: 600; line-height: 1.1; }
  .agent__title { font-size: 13px; opacity: 0.9; }
  .contact {
    position: absolute; list-style: none;
    font-size: 13.5px; line-height: 20px; letter-spacing: 0.3px;
  }
  .contact--office { left: 430px; top: 218px; }
  .contact--primary { left: 125px; top: 268px; }
  .contact li { display: flex; align-items: flex-start; gap: 7px; white-space: nowrap; }
  .contact svg { width: 12px; height: 12px; margin-top: 4px; flex: none; fill: currentColor; }
  .contact .indent { padding-left: 19px; }
  .contact .web { letter-spacing: 1.5px; }

  /* Back */
  .card--back { top: 540px; background: var(--paper); color: var(--navy); }
  .back__band {
    position: absolute; left: 0; bottom: 0;
    width: 100%; height: 50px; background: var(--navy);
  }
  .back__brand {
    position: absolute; left: 60px; top: 70px;
    font-weight: 600; font-size: 40px; line-height: 1;
  }
  .back__rule {
    position: absolute; left: 60px; top: 122px;
    width: 250px; height: 2px; background: var(--rule-grey);
  }
  .appointment { position: absolute; left: 380px; top: 70px; width: 270px; }
  .appointment__title { font-size: 22px; font-weight: 600; margin-bottom: 22px; }
  .appointment__field {
    display: flex; align-items: flex-end; gap: 10px;
    font-size: 16px; margin-bottom: 28px;
  }
  .appointment__label { width: 44px; }
  .appointment__line { flex: 1; height: 1px; background: var(--navy); margin-bottom: 5px; }
</style>
</head>
<body>
  <article class="card card--front">
    <div class="front__band"></div>
    <div class="front__tab front__tab--left"></div>
    <div class="front__tab front__tab--right"></div>
    <div class="front__dot"></div>

    <div class="brand-name">Birchford Realty</div>
    <div class="brand-rule"></div>

    <div class="company">
      <div class="company__name">Birchford Realty</div>
      <div class="company__license">Broker License Number: 5839162</div>
      <div class="agent">
        <div class="agent__name">Dana Whitlock</div>
        <div class="agent__title">Licensed Real Estate Broker</div>
      </div>
    </div>

    <ul class="contact contact--office">
      <li>
        <svg viewBox="0 0 16 16" aria-hidden="true"><path d="M1 5c0-2 3-3 7-3s7 1 7 3v1h-4V5H5v1H1zM3 7h10l1 7H2z"/></svg>
        <span>Office +098-555-0143</span>
      </li>
      <li>
        <svg viewBox="0 0 16 16" aria-hidden="true"><path d="M8 0a5 5 0 0 1 5 5c0 4-5 11-5 11S3 9 3 5a5 5 0 0 1 5-5zm0 3a2 2 0 1 0 0 4 2 2 0 0 0 0-4z"/></svg>
        <span>7218 Crestover Ave E</span>
      </li>
      <li class="indent">Saginaw, MI 48271</li>
    </ul>

    <ul class="contact contact--primary">
      <li>
        <svg viewBox="0 0 16 16" aria-hidden="true"><path d="M1 5c0-2 3-3 7-3s7 1 7 3v1h-4V5H5v1H1zM3 7h10l1 7H2z"/></svg>
        <span>Cell +123-555-0190</span>
      </li>
      <li>
        <svg viewBox="0 0 16 16" aria-hidden="true"><path d="M1 3h14v10H1zm1 1 6 5 6-5z"/></svg>
        <span>dana.whitlock@BirchfordRealty.example</span>
      </li>
      <li>
        <svg viewBox="0 0 16 16" aria-hidden="true"><path d="M8 1a7 7 0 1 0 0 14A7 7 0 0 0 8 1zm0 1.5a5.5 5.5 0 1 1 0 11 5.5 5.5 0 0 1 0-11zM2 7.3h12v1.4H2zM7.3 2h1.4v12H7.3z"/></svg>
        <span class="web">WWW.BirchfordRealty.example</span>
      </li>
    </ul>
  </article>

  <article class="card card--back">
    <div class="back__brand">Birchford Realty</div>
    <div class="back__rule"></div>

    <section class="appointment">
      <div class="appointment__title">Your Appointment</div>
      <div class="appointment__field">
        <span class="appointment__label">Date</span><span class="appointment__line"></span>
      </div>
      <div class="appointment__field">
        <span class="appointment__label">Time</span><span class="appointment__line"></span>
      </div>
    </section>

    <div class="back__band"></div>
  </article>
</body>
</html>
```